Post storm repair flyer

looking for an eye catching 6x9 postcard to send out to single family home owners advertising a "Post Storm Repair Special" explaining that after the recent hurricanes its very important to have your roof checked and any repairs fixed right away before they become a bigger more costly problem and that even though your home wasn't directly hit by the storm the high wind gust could've cause unseen damage.
offer $200 off any repair *some rules may apply
Lark Roofing
888.417.LARK
www.LarkRoofing.example

Roofing

```html
<!DOCTYPE html>
<html lang="en">
<head>
<meta charset="utf-8">
<title>Lark Roofing – Post Storm Repair Special</title>
<link rel="stylesheet" href="https://fonts.googleapis.com/css2?family=Bebas+Neue&family=Poppins:wght@400;600;700&display=swap">
<style>
  :root{
    --stage:#8c8c8c;
    --gold:#e2a935;
    --ink:#111111;
    --charcoal:#2b2b2b;
    --white:#ffffff;
    --paper:#ffffff;
  }
  *{box-sizing:border-box;margin:0;padding:0}
  html,body{width:1200px;height:449px;overflow:hidden;background:var(--stage)}
  .stage{position:relative;width:1200px;height:449px}
  .card{position:absolute;top:40px;width:554px;height:369px;background:var(--paper);overflow:hidden}
  .card--front{left:38px}
  .card--back{left:608px}

  /* front */
  .front-photo{position:absolute;left:0;top:0;width:554px;height:327px;
    background:linear-gradient(160deg,#3d3f42 0%,#2a2b2d 45%,#1c1d1f 100%)}
  .front-shapes{position:absolute;left:0;top:0}
  .headline{position:absolute;left:33px;top:28px;font-family:"Bebas Neue",sans-serif;
    font-size:58px;line-height:47px;color:var(--white);letter-spacing:.5px}
  .headline .accent{color:var(--gold)}
  .headline-rule{position:absolute;left:33px;top:133px;width:53px;height:1px;background:var(--white)}
  .intro{position:absolute;left:33px;top:142px;width:330px;font-family:"Poppins",sans-serif;
    font-size:9.4px;line-height:14.4px;color:var(--white)}
  .offer{position:absolute;left:0;top:226px;width:176px;text-align:center;font-family:"Bebas Neue",sans-serif}
  .offer-label{font-size:24px;line-height:22px;color:var(--white)}
  .offer-amount{font-size:38px;line-height:32px;color:var(--ink)}
  .offer-scope{font-size:24px;line-height:22px;color:var(--white)}
  .offer-note{font-family:"Poppins",sans-serif;font-size:8px;line-height:14px;color:var(--ink)}
  .brand-name{position:absolute;left:380px;top:266px;width:160px;text-align:center;
    font-family:"Poppins",sans-serif;font-weight:700;font-size:17px;color:var(--ink)}

  /* footer */
  .contact-bar{position:absolute;left:0;bottom:0;width:554px;height:42px;background:var(--paper);
    display:flex;align-items:center;justify-content:center;gap:22px;
    font-family:"Poppins",sans-serif;font-weight:600;font-size:15.5px;color:var(--ink)}
  .contact-bar .divider{color:var(--gold);font-weight:400}

  /* back */
  .back-photo{position:absolute;left:0;top:0;width:277px;height:327px;
    background:linear-gradient(170deg,#6e5a48 0%,#4a4a4f 35%,#3a3c40 100%)}
  .back-panel{position:absolute;left:0;top:135px;width:277px;height:192px;background:rgba(28,28,30,.86)}
  .tagline{position:absolute;left:32px;top:158px;font-family:"Bebas Neue",sans-serif;color:var(--white)}
  .tagline-lead{font-size:30px;line-height:25px}
  .tagline-call{font-size:63px;line-height:52px;margin-top:4px}
  .tagline-call .accent{color:var(--gold)}
  .corner-stripe{position:absolute;right:0;top:0}
  .back-brand{position:absolute;right:16px;top:288px;font-family:"Poppins",sans-serif;
    font-weight:700;font-size:11px;color:var(--gold)}
</style>
</head>
<body>
<main class="stage">

  <section class="card card--front">
    <div class="front-photo" role="img" aria-label="Dusk photo of a two-storey family home with gabled roof, darkened behind the text"></div>
    <svg class="front-shapes" width="554" height="327" viewBox="0 0 554 327" aria-hidden="true">
      <polygon points="0,249 115,216 386,327 0,327" fill="var(--gold)"/>
      <polygon points="196,216 554,216 554,327 386,327" fill="var(--gold)"/>
    </svg>
    <h1 class="headline">Post Storm<br>Repair <span class="accent">Special</span></h1>
    <div class="headline-rule"></div>
    <p class="intro">After the recent hurricanes, it's important to check your roof and fix any repairs quickly before they become a bigger more costly problem. Even if your home wasn't hit directly, strong winds might have caused hidden damage.</p>
    <div class="offer">
      <div class="offer-label">Offer</div>
      <div class="offer-amount">$200 Off</div>
      <div class="offer-scope">Any Repair</div>
      <div class="offer-note">*some rules may apply</div>
    </div>
    <div class="brand-name">LARK ROOFING</div>
    <footer class="contact-bar">
      <span>Lark Roofing</span><span class="divider">|</span>
      <span>888.417.LARK</span><span class="divider">|</span>
      <span>www.LarkRoofing.example</span>
    </footer>
  </section>

  <section class="card card--back">
    <div class="back-photo" role="img" aria-label="Photo of a house with shingled roof, lit windows and a leafy branch"></div>
    <div class="back-panel"></div>
    <div class="tagline">
      <div class="tagline-lead">You worked hard<br>building your home.</div>
      <div class="tagline-call"><span class="accent">Protect</span><br>your nest!</div>
    </div>
    <svg class="corner-stripe" width="80" height="45" viewBox="0 0 80 45" aria-hidden="true">
      <polygon points="6,0 49,0 80,21 80,41" fill="var(--gold)"/>
    </svg>
    <div class="back-brand">Lark Roofing</div>
    <footer class="contact-bar">
      <span>Lark Roofing</span><span class="divider">|</span>
      <span>888.417.LARK</span><span class="divider">|</span>
      <span>www.LarkRoofing.example</span>
    </footer>
  </section>

</main>
</body>
</html>
```